Computer repair services flyer

This flyer / leaflet is required to promote my local computer and laptop repair business. It will primarily be used for pinning to notice boards when I get access to shared accommodation but I will also use it in the future for posting through letterboxes in affluent areas.

Company branding, logo, services, pricing, contact details etc. can be found on my website at : www.brightlanetech.co.uk

The services I would predominantly like to promote on this flyer are :

Speeding up slow / old computers
Virus removal
Lost data recovered
Broken laptop screen replacements
Dead laptops fixed
We buy and recycle broken laptops for cash

Other features to highlight :

Friendly and experienced
We are local (Near to Cardiff city center)
Quick repair turnaround - most repairs within 24hours
Affordable / No VAT
Free diagnostics
No Fix = No fee
Free collection and delivery
We Guarantee our work

Calls to action and attention grabbing if possible. Offer 10% off. Free cooling fan clean.

Size of flyer = A5 (210 x 148mm or 8.3 x 5.8in) portrait, single sided colour.

Target Market(s)

18 to 60 years

Industry/Entity Type

Accommodation

Requirements
Must have
• 02940 613857

```html
<!DOCTYPE html>
<html lang="en">
<head>
<meta charset="utf-8">
<title>Bright Lane Tech – Computer Repair Flyer</title>
<link rel="stylesheet" href="https://fonts.googleapis.com/css2?family=Arimo:wght@700&family=Oswald:wght@600;700&family=Roboto+Condensed:wght@700&family=Pinyon+Script&display=swap">
<style>
  :root {
    --orange: #f47b20;
    --orange-deep: #e8501a;
    --yellow: #f7b500;
    --charcoal: #3d3d3f;
    --black: #0d0d0d;
    --grey-band: #a7a9ac;
    --grey-light: #e7e7e8;
    --white: #ffffff;
    --page: #f4f4f4;
  }
  * { box-sizing: border-box; margin: 0; padding: 0; }
  html, body { width: 939px; height: 1200px; overflow: hidden; }
  body { background: var(--page); font-family: "Arimo", Arial, sans-serif; font-weight: 700; }

  .flyer {
    position: absolute; left: 102px; top: 113px;
    width: 733px; height: 1027px;
    background: var(--white); border: 1px solid #c9c9c9; overflow: hidden;
  }
  .flyer-art { position: absolute; inset: 0; }
  .abs { position: absolute; }

  .brand { left: 38px; top: 70px; display: flex; align-items: flex-start; gap: 14px; }
  .brand-dot { width: 40px; height: 40px; border-radius: 50%; background: var(--orange); margin-top: 8px; }
  .brand-name { color: var(--orange); font-size: 52px; line-height: 1; letter-spacing: -1px; }

  .address { left: 468px; top: 66px; font-size: 15px; line-height: 19px; font-style: normal; color: var(--black); }
  .phone { left: 466px; top: 152px; font-family: "Oswald", sans-serif; font-weight: 700; font-size: 44px; line-height: 1; letter-spacing: -0.5px; color: var(--black); white-space: nowrap; }

  .photo-hand { left: 578px; top: 0; width: 155px; height: 142px; background: linear-gradient(160deg, #eaeaea, #8a8c90 50%, #1f2023); }
  .photo-laptop { left: 368px; top: 467px; width: 365px; height: 370px; background: linear-gradient(150deg, #c8ccd6, #8e94a6 45%, #eceef0 75%, #bfc1c4); }
  .photo-mouse { left: 3px; top: 872px; width: 115px; height: 90px; background: linear-gradient(135deg, #d6d7d9, #9fa1a5 60%, #e7c98a); }

  .features { left: 31px; top: 270px; list-style: none; font-size: 20px; line-height: 25px; color: var(--black); }
  .features li { position: relative; padding-left: 17px; margin-bottom: 14.5px; }
  .features li::before { content: ""; position: absolute; left: 0; top: 9px; width: 8px; height: 8px; border-radius: 50%; background: var(--black); }

  .offer-value { left: 36px; top: 682px; font-family: "Oswald", sans-serif; font-weight: 700; font-size: 120px; line-height: 1; color: var(--orange); letter-spacing: -3px; }
  .offer-percent { left: 146px; top: 736px; font-family: "Oswald", sans-serif; font-weight: 700; font-size: 62px; line-height: 1; color: var(--orange); }
  .offer-word { left: 146px; top: 680px; font-family: "Pinyon Script", cursive; font-size: 54px; line-height: 1; font-weight: 400; color: var(--black); }
  .offer-note { left: 50px; top: 807px; font-size: 13px; color: var(--black); }

  .service { width: 100px; height: 112px; display: flex; align-items: center; justify-content: center; text-align: center; color: var(--white); font-family: "Roboto Condensed", sans-serif; font-size: 20px; line-height: 24px; }

  .buy-recycle { left: 490px; top: 312px; width: 245px; text-align: center; color: var(--white); font-family: "Roboto Condensed", sans-serif; line-height: 1.25; }
  .buy-recycle .line { display: block; font-size: 28px; }
  .buy-recycle .broken { display: block; font-size: 40px; line-height: 1.05; }
  .buy-recycle .tail { display: block; font-size: 27px; }

  .screen-repair { color: var(--white); font-size: 25px; line-height: 32px; }

  .website { left: 31px; top: 982px; font-size: 22px; color: var(--black); }
</style>
</head>
<body>
  <main class="flyer">
    <svg class="flyer-art" width="733" height="1027" viewBox="0 0 733 1027" aria-hidden="true">
      <defs>
        <linearGradient id="panelGrey" x1="0" y1="0" x2="0" y2="1">
          <stop offset="0" stop-color="#f7f7f7"/>
          <stop offset="1" stop-color="#dedede"/>
        </linearGradient>
        <linearGradient id="panelOrange" x1="0" y1="0" x2="1" y2="1">
          <stop offset="0" stop-color="#f7941d"/>
          <stop offset=".6" stop-color="#ef6a1c"/>
          <stop offset="1" stop-color="#e8501a"/>
        </linearGradient>
      </defs>
      <rect class="band" x="0" y="232" width="733" height="17" fill="var(--grey-band)"/>
      <rect class="panel-left" x="0" y="249" width="733" height="726" fill="url(#panelGrey)"/>
      <path class="swoosh-grey" d="M380,249 C230,410 220,760 330,975" fill="none" stroke="#c8c9cb" stroke-width="26"/>
      <path class="swoosh-white" d="M398,249 C255,410 248,760 352,975" fill="none" stroke="#ffffff" stroke-width="12"/>
      <path class="panel-orange" d="M420,249 H733 V975 H370 C270,760 275,420 420,249 Z" fill="url(#panelOrange)"/>
      <path class="swoosh-inner" d="M440,249 C300,420 300,760 400,975" fill="none" stroke="#9a9b9e" stroke-width="16" opacity=".85"/>
      <rect class="screen-box" x="473" y="847" width="260" height="130" fill="var(--black)"/>
      <path class="swoosh-base" d="M280,975 C380,990 440,955 480,900" fill="none" stroke="#9a9b9e" stroke-width="18"/>
      <rect class="footer" x="0" y="975" width="733" height="52" fill="var(--white)"/>
      <path class="footer-accent" d="M300,975 C420,1000 480,1010 560,975 Z" fill="var(--orange)" opacity=".7"/>

      <g class="service-halos">
        <circle cx="457" cy="334" r="74" fill="#ffffff" opacity=".28"/>
        <circle cx="346" cy="477" r="74" fill="#ffffff" opacity=".28"/>
        <circle cx="316" cy="677" r="74" fill="#ffffff" opacity=".28"/>
        <circle cx="387" cy="887" r="74" fill="#ffffff" opacity=".28"/>
      </g>
    </svg>

    <div class="abs photo-laptop" role="img" aria-label="Photo of a silver laptop with a shattered screen"></div>

    <svg class="flyer-art" width="733" height="1027" viewBox="0 0 733 1027" aria-hidden="true">
      <g class="service-badges">
        <circle cx="457" cy="334" r="56" fill="var(--charcoal)" stroke="var(--yellow)" stroke-width="7"/>
        <circle cx="346" cy="477" r="56" fill="var(--charcoal)" stroke="var(--yellow)" stroke-width="7"/>
        <circle cx="316" cy="677" r="56" fill="var(--charcoal)" stroke="var(--yellow)" stroke-width="7"/>
        <circle cx="387" cy="887" r="56" fill="var(--charcoal)" stroke="var(--yellow)" stroke-width="7"/>
      </g>
    </svg>

    <header>
      <div class="abs brand">
        <span class="brand-dot"></span>
        <span class="brand-name">Bright Lane<br>Tech</span>
      </div>
      <address class="abs address">14 Marlow Rd,<br>Llanishen,<br>Cardiff,<br>CF14 7QA</address>
      <div class="abs phone">02940 613857</div>
      <div class="abs photo-hand" role="img" aria-label="Photo of a hand in a suit sleeve holding a telephone handset"></div>
    </header>

    <ul class="abs features">
      <li>Friendly and experienced</li>
      <li>We are Near to Cardiff city</li>
      <li>Quick repair turnaround<br>repairs within 24hours</li>
      <li>Affordable/No VAT</li>
      <li>Free diagnostics</li>
      <li>No Fix = No fee</li>
      <li>Free collection &amp;<br>delivery</li>
      <li>We Guarantee<br>our work</li>
    </ul>

    <div class="abs offer-value">10</div>
    <div class="abs offer-percent">%</div>
    <div class="abs offer-word">Off</div>
    <div class="abs offer-note">Free cooling fan clean.</div>

    <div class="abs service" style="left:407px;top:278px;">Virus<br>Removal</div>
    <div class="abs service" style="left:296px;top:421px;">Lost Data<br>Recovered</div>
    <div class="abs service" style="left:266px;top:621px;">Speeding<br>up slow<br>Computer</div>
    <div class="abs service" style="left:337px;top:831px;font-size:23px;line-height:28px;">Dead<br>Loptops<br>Fixed</div>

    <div class="abs buy-recycle">
      <span class="line">We Buy</span>
      <span class="line">&amp; Recycle</span>
      <span class="broken">BROKEN</span>
      <span class="tail">Laptop for Cash</span>
    </div>

    <div class="abs screen-repair" style="left:508px;top:873px;">Broken Laptop</div>
    <div class="abs screen-repair" style="left:528px;top:905px;">Screen</div>
    <div class="abs screen-repair" style="left:564px;top:937px;">Replacement</div>

    <div class="abs photo-mouse" role="img" aria-label="Illustration of a grey and orange computer mouse"></div>

    <div class="abs website">www.brightlanetech.co.uk</div>
  </main>
</body>
</html>
```